Brochure design for trade company

I would like to get a professional, easy to read and eye catchy capability statement designed for my electrical business.

My aim is to be able to go to property managers and WOW them when they see the capability statement.

Attached the content writing, design brief, company logo and template of what I like below. If there are any questions please send me a message.

The areas we service photo is an example, please do your own designs for the maps section

Thank you in advance for the help team.

Requirements
Must have
• The areas we service photo is an example, please do your own designs for the maps section
Nice to have
• Eye catching and creative. Also be warm & inviting
Should not have
• Not too out of place looking photos or elements. Don’t make it he design look too cold

```html
<!DOCTYPE html>
<html lang="en">
<head>
<meta charset="utf-8">
<title>Voltline Electrical – Capability Statement</title>
<link href="https://fonts.googleapis.com/css2?family=Bebas+Neue&family=Barlow:wght@400;500&display=swap" rel="stylesheet">
<style>
  :root {
    --backdrop: #c4c4c4;
    --black: #0b0b0b;
    --orange: #e99b3d;
    --sun-top: #e4723e;
    --sun-mid: #f29a2e;
    --sun-low: #f8cf45;
    --white: #ffffff;
    --blue: #13a9e6;
    --green: #8cc63f;
    --pink: #e6087f;
    --gold: #c98a3c;
  }
  * { box-sizing: border-box; margin: 0; padding: 0; }
  html, body { width: 1200px; height: 2260px; overflow: hidden; }
  body { background: var(--backdrop); position: relative; font-family: "Barlow", sans-serif; }

  .page {
    position: absolute; left: 232px; width: 734px; height: 1038px;
    overflow: hidden; box-shadow: 6px 6px 10px rgba(0,0,0,0.35);
  }
  .page--cover { top: 56px; }
  .page--about { top: 1144px; }

  /* Cover */
  .cover-header {
    position: absolute; inset: 0 0 auto 0; height: 192px; background: var(--black);
    display: flex; align-items: center; justify-content: center;
  }
  .brand-name {
    font-family: "Bebas Neue", sans-serif; font-size: 64px; letter-spacing: 4px;
    color: var(--white); line-height: 1;
  }
  .cover-photo {
    position: absolute; top: 192px; left: 0; right: 0; bottom: 0;
    background: linear-gradient(180deg, var(--sun-top) 0%, var(--sun-mid) 38%, var(--sun-low) 68%, var(--sun-mid) 100%);
  }
  .cover-title {
    position: absolute; top: 262px; left: 0; right: 0; text-align: center;
    font-family: "Bebas Neue", sans-serif; font-size: 142px; line-height: 0.86;
    color: var(--black); letter-spacing: 1px;
  }
  .cover-tagline {
    position: absolute; top: 553px; left: 0; right: 0; text-align: center;
    font-family: "Bebas Neue", sans-serif; font-size: 40px; letter-spacing: 1px; color: var(--black);
  }
  .sector-bar {
    position: absolute; top: 699px; left: 99px; width: 535px; height: 51px;
    background: var(--black); color: var(--white);
    display: flex; align-items: center; justify-content: center; gap: 10px;
    font-family: "Bebas Neue", sans-serif; font-size: 28px; letter-spacing: 0.5px;
  }
  .sector-bar .divider { width: 2px; height: 26px; background: var(--white); }
  .cover-web {
    position: absolute; top: 937px; left: 0; right: 0; text-align: center;
    font-family: "Bebas Neue", sans-serif; font-size: 30px; color: var(--black);
  }

  /* About page */
  .about-intro {
    position: absolute; inset: 0 0 auto 0; height: 392px; background: var(--orange);
    padding: 52px 65px 0; color: var(--white);
  }
  .about-heading { font-family: "Bebas Neue", sans-serif; font-size: 42px; letter-spacing: 0.5px; line-height: 1; }
  .about-sub { font-size: 30px; font-weight: 400; margin-top: 22px; line-height: 1; }
  .about-copy { margin-top: 16px; font-size: 14.5px; line-height: 19.5px; width: 600px; }
  .about-copy p + p { margin-top: 19px; }

  .values-photo {
    position: absolute; top: 392px; left: 0; right: 0; bottom: 0;
    background: linear-gradient(180deg, #141718 0%, #1d2022 45%, #23211d 80%, #0f0c08 100%);
  }
  .values-title {
    position: absolute; top: 640px; left: 67px; color: var(--white);
    font-size: 50px; line-height: 50px; font-weight: 400; letter-spacing: 1px;
  }
  .values-links { position: absolute; inset: 0; }
  .value-pill {
    position: absolute; left: 386px; width: 253px; height: 62px; border-radius: 31px;
    color: var(--white); font-size: 17px; line-height: 22px; text-align: center;
    display: flex; align-items: center; justify-content: center; padding: 0 40px;
  }
  .value-pill--safety { top: 478px; background: var(--orange); }
  .value-pill--community { top: 583px; background: var(--blue); }
  .value-pill--customer { top: 688px; background: var(--green); }
  .value-pill--openness { top: 795px; background: var(--pink); }

  .footer-web {
    position: absolute; top: 956px; left: 86px; width: 563px; height: 48px;
    background: linear-gradient(90deg, rgba(201,138,60,0) 0%, var(--gold) 20%, var(--gold) 80%, rgba(201,138,60,0) 100%);
    display: flex; align-items: center; justify-content: center;
    font-family: "Bebas Neue", sans-serif; font-size: 18px; letter-spacing: 4px; color: var(--white);
  }
</style>
</head>
<body>

<section class="page page--cover">
  <header class="cover-header">
    <div class="brand-name">Voltline Electrical</div>
  </header>
  <div class="cover-photo" role="img" aria-label="Electricity transmission pylons silhouetted against an orange and yellow sunset sky"></div>
  <h1 class="cover-title">Capability<br>Statement</h1>
  <p class="cover-tagline">When quality and reliability counts</p>
  <div class="sector-bar">
    <span>Residential</span><span class="divider"></span>
    <span>Commercial</span><span class="divider"></span>
    <span>Real Estate</span><span class="divider"></span>
    <span>Strata</span>
  </div>
  <p class="cover-web">voltlineelectrical.com.au</p>
</section>

<section class="page page--about">
  <div class="about-intro">
    <h2 class="about-heading">About Voltline Electrical</h2>
    <h3 class="about-sub">Who we are</h3>
    <div class="about-copy">
      <p>Voltline Electrical, we’re more than just a team of electricians—we’re your extended family that you can rely on 24/7 for reliable, expert help for anything electrical related.</p>
      <p>With our friendly, reliable, and no-nonsense approach, we ensure that your needs are met with professionalism and a smile.<br>Whether it’s a small repair or a major installation, we’re here to make your life easier.</p>
      <p>At Voltline Electrical, we make sure that every job counts.</p>
    </div>
  </div>

  <div class="values-photo" role="img" aria-label="Dark dusk photograph of a transmission tower over a landscape"></div>
  <h2 class="values-title">CORE<br>VALUES</h2>
  <svg class="values-links" width="734" height="1038" viewBox="0 0 734 1038" aria-hidden="true">
    <g stroke-width="4" fill="none" stroke-linecap="round">
      <line x1="265" y1="671" x2="376" y2="519" stroke="#e99b3d"/>
      <line x1="265" y1="671" x2="380" y2="627" stroke="#13a9e6"/>
      <line x1="265" y1="671" x2="380" y2="711" stroke="#8cc63f"/>
      <line x1="265" y1="671" x2="376" y2="833" stroke="#e6087f"/>
    </g>
  </svg>
  <div class="value-pill value-pill--safety">Reliability and safety first</div>
  <div class="value-pill value-pill--community">Community and respect</div>
  <div class="value-pill value-pill--customer">Customer Focused</div>
  <div class="value-pill value-pill--openness">Openness, trust and accountability</div>

  <div class="footer-web">voltlineelectrical.com.au</div>
</section>

</body>
</html>
```